Mara Quill
Senior Administrator
Modern
P.O. Box 742
Maplebrook, PA
bwsaquill@postlark.com
www.thebrightwaystudyacademy.com
please use this on front of card

```html
<!DOCTYPE html>
<html lang="en">
<head>
<meta charset="utf-8">
<title>The Brightway Study Academy – Business Card</title>
<link href="https://fonts.googleapis.com/css2?family=Open+Sans:wght@400;600;700&display=swap" rel="stylesheet">
<style>
  :root {
    --page: #f4f4f4;
    --card: #ffffff;
    --brand-blue: #2a8ccf;
    --ink: #3c3c3c;
    --muted: #6d6d6d;
    --rule: #b9c7d3;
    --band-text: #ffffff;
  }
  * { box-sizing: border-box; margin: 0; padding: 0; }
  html, body {
    width: 1200px; height: 331px; overflow: hidden;
    background: var(--page);
    font-family: "Open Sans", Arial, sans-serif;
  }
  .sheet {
    position: relative; width: 1200px; height: 331px;
    display: flex; justify-content: space-between; align-items: center;
    padding: 0 6px;
  }
  .card {
    position: relative; width: 570px; height: 322px;
    background: var(--card);
    box-shadow: 0 1px 4px rgba(0,0,0,.18);
    overflow: hidden;
  }
  .brand {
    position: absolute; display: flex; align-items: center; gap: 10px;
  }
  .brand-dot {
    flex: none; width: 48px; height: 48px; border-radius: 50%;
    background: var(--brand-blue);
  }
  .brand-text { display: flex; flex-direction: column; }
  .brand-name {
    font-weight: 700; font-size: 24px; line-height: 1.05;
    color: var(--ink); letter-spacing: .2px;
  }
  .brand-tagline {
    margin-top: 5px; font-size: 7.5px; font-weight: 600;
    letter-spacing: .6px; color: var(--muted); text-transform: uppercase;
    white-space: nowrap;
  }
  .card-front .brand { left: 22px; top: 112px; }
  .card-back .brand { left: 160px; top: 118px; }
  .divider {
    position: absolute; left: 303px; top: 40px; width: 1px; height: 220px;
    background: var(--rule);
  }
  .contact {
    position: absolute; left: 322px; top: 60px;
    color: var(--ink); font-size: 13px; line-height: 1.35;
    font-style: normal;
  }
  .contact .name { font-size: 17px; font-weight: 600; }
  .contact .role { color: var(--muted); margin-bottom: 22px; }
  .band {
    position: absolute; left: 0; right: 0; bottom: 0; height: 18px;
    background: var(--brand-blue);
    color: var(--band-text); font-size: 10.5px; line-height: 18px;
    text-align: center;
  }
</style>
</head>
<body>
  <main class="sheet">
    <section class="card card-front">
      <div class="brand">
        <span class="brand-dot"></span>
        <div class="brand-text">
          <span class="brand-name">The Brightway<br>Study Academy</span>
          <span class="brand-tagline">Education | Apprenticeship | Career</span>
        </div>
      </div>
      <div class="divider"></div>
      <address class="contact">
        <div class="name">Mara Quill</div>
        <div class="role">Senior Administrator</div>
        <div>P.O. Box 742</div>
        <div>Maplebrook, PA</div>
        <div>17520</div>
        <div>Toll free : 800-555-0147</div>
        <div>Email : bwsaquill@postlark.com</div>
      </address>
      <div class="band">www.thebrightwaystudyacademy.com</div>
    </section>

    <section class="card card-back">
      <div class="brand">
        <span class="brand-dot"></span>
        <div class="brand-text">
          <span class="brand-name">The Brightway<br>Study Academy</span>
          <span class="brand-tagline">Education | Apprenticeship | Career</span>
        </div>
      </div>
      <div class="band">www.thebrightwaystudyacademy.com</div>
    </section>
  </main>
</body>
</html>
```